Trivesso needs a new design we have an updated logo and want a high qualitative high end feel

feel and aesthetic should be high qualitative like the packaging in a zuvi or the qualatative weight/feel of an zuvi design. modern, elegant bold.probably just the trivesso logo on the backone vesion could be blue background white letter ... open to ideas
Target Market(s)
legal, insurance , medical, finance rho 740
Industry/Entity Type
Information Technology
Font styles to use
Serif

```html
<!DOCTYPE html>
<html lang="en">
<head>
<meta charset="UTF-8">
<title>Trivesso — Business Card</title>
<link href="https://fonts.googleapis.com/css2?family=Montserrat:wght@500;600;700&display=swap" rel="stylesheet">
<style>
  :root {
    --navy: #1b2c3f;
    --navy-light: #34495d;
    --ink: #1d2b3a;
    --paper: #ffffff;
    --stage: #e9eaec;
    --muted: #2a3746;
  }
  * { box-sizing: border-box; margin: 0; padding: 0; }
  html, body {
    width: 1200px; height: 900px; overflow: hidden;
    background: var(--stage);
    font-family: "Montserrat", Arial, sans-serif;
  }
  .canvas { position: relative; width: 1200px; height: 900px; }
  .card {
    position: absolute; left: 280px;
    width: 640px; height: 366px;
    box-shadow: 0 10px 30px rgba(0,0,0,0.15);
  }
  .card--back {
    top: 70px;
    background: linear-gradient(135deg, var(--navy) 0%, var(--navy) 45%, var(--navy-light) 100%);
    display: flex; align-items: center; justify-content: center;
  }
  .card--front {
    top: 464px;
    background: var(--paper);
    display: flex; align-items: center;
  }
  .wordmark { font-weight: 600; letter-spacing: 0.5px; line-height: 1; white-space: nowrap; }
  .card--back .wordmark { color: var(--paper); font-size: 72px; }
  .front-brand { width: 50%; display: flex; justify-content: center; }
  .card--front .wordmark { color: var(--ink); font-size: 46px; }
  .divider { width: 2px; height: 180px; background: var(--ink); }
  .contact { padding-left: 34px; color: var(--ink); }
  .contact__name { font-size: 26px; font-weight: 700; letter-spacing: 1px; }
  .contact__title { font-size: 17px; font-weight: 700; letter-spacing: 1px; margin-top: 2px; }
  .contact__list { list-style: none; margin-top: 22px; }
  .contact__item {
    display: flex; align-items: center; gap: 14px;
    font-size: 19px; font-weight: 500; color: var(--muted);
    margin-bottom: 8px; white-space: nowrap;
  }
  .contact__icon { width: 16px; height: 16px; flex: none; }
</style>
</head>
<body>
<main class="canvas">
  <section class="card card--back">
    <span class="wordmark">trivesso</span>
  </section>

  <section class="card card--front">
    <div class="front-brand">
      <span class="wordmark">trivesso</span>
    </div>
    <div class="divider"></div>
    <div class="contact">
      <h1 class="contact__name">YOUR NAME</h1>
      <p class="contact__title">JOB TITLE</p>
      <ul class="contact__list">
        <li class="contact__item">
          <svg class="contact__icon" viewBox="0 0 16 16"><path d="M4 1 L6.5 4.5 L5 6.5 Q6.5 9.5 9.5 11 L11.5 9.5 L15 12 L13 15 Q5 14 1 3 Z" fill="var(--ink)"/></svg>
          000 000 0000
        </li>
        <li class="contact__item">
          <svg class="contact__icon" viewBox="0 0 16 16"><rect x="1" y="3" width="14" height="10" fill="var(--ink)"/><path d="M1 3 L8 9 L15 3" stroke="#fff" stroke-width="1.2" fill="none"/></svg>
          youremail@xyz.com
        </li>
        <li class="contact__item">
          <svg class="contact__icon" viewBox="0 0 16 16" fill="none" stroke="var(--ink)" stroke-width="1.2"><circle cx="8" cy="8" r="6.5"/><ellipse cx="8" cy="8" rx="3" ry="6.5"/><line x1="1.5" y1="8" x2="14.5" y2="8"/></svg>
          www.yourwebsite.com
        </li>
      </ul>
    </div>
  </section>
</main>
</body>
</html>
```